Design a For Sale sign board and Direction Sign Board.
Attached is an example of what i am thinking but am happy to look at any options.
Colours are to be ""bright Orange"on white and in reverse as well.

Logo id Fairbrook & Co Real Estate.

```html
<!DOCTYPE html>
<html lang="en">
<head>
<meta charset="utf-8">
<title>Fairbrook &amp; Co Real Estate – For Sale Sign</title>
<link rel="stylesheet" href="https://fonts.googleapis.com/css2?family=Jost:wght@600;700&display=swap">
<style>
  :root {
    --brand-yellow: #fdc218;
    --ink-black: #000000;
    --board-white: #ffffff;
    --backdrop: #e6e6e6;
    --suit-blue-light: #6f86b8;
    --suit-blue-dark: #3c4f86;
  }
  * { box-sizing: border-box; margin: 0; padding: 0; }
  html, body {
    width: 1200px; height: 1200px; overflow: hidden;
    background: var(--backdrop);
    font-family: "Jost", "Futura", sans-serif;
  }
  .sign-board {
    position: absolute; left: 30px; top: 191px;
    width: 1140px; height: 818px;
    background: var(--board-white);
    overflow: hidden;
    box-shadow: 0 6px 18px rgba(0,0,0,0.18);
  }
  .header-swoosh { position: absolute; inset: 0; }
  .sale-heading {
    position: absolute; left: 96px; top: 72px;
    font-size: 92px; font-weight: 700; line-height: 1;
    color: var(--board-white); letter-spacing: -1px;
    white-space: nowrap;
  }
  .agency-name {
    position: absolute; left: 590px; top: 86px; width: 450px;
    color: var(--board-white); font-weight: 600; text-align: center;
    line-height: 1; white-space: nowrap;
  }
  .agency-name .agency-title { display: block; font-size: 50px; }
  .agency-name .agency-sub { display: block; font-size: 26px; letter-spacing: 7px; margin-top: 14px; }
  .agent-photo {
    position: absolute; left: 730px; top: 291px;
    width: 410px; height: 527px;
    background: linear-gradient(180deg, var(--suit-blue-light) 0%, var(--suit-blue-dark) 100%);
    border-radius: 160px 160px 0 0;
  }
  .agent-name {
    position: absolute; left: 52px; top: 540px;
    font-size: 88px; font-weight: 700; line-height: 1;
    color: var(--brand-yellow); letter-spacing: -1px;
    white-space: nowrap;
  }
  .agent-phone {
    position: absolute; left: 55px; top: 673px;
    width: 653px; height: 101px;
    background: var(--brand-yellow);
    color: var(--board-white);
    font-size: 88px; font-weight: 700; line-height: 101px;
    padding-left: 16px; letter-spacing: -1px;
    white-space: nowrap; overflow: hidden;
  }
</style>
</head>
<body>
  <div class="sign-board">
    <svg class="header-swoosh" width="1140" height="818" viewBox="0 0 1140 818" aria-hidden="true">
      <path d="M0 0 H1140 V275 C800 256 330 290 0 500 Z" fill="var(--ink-black)"/>
      <path d="M0 0 H1140 V268 C800 238 350 250 0 425 Z" fill="var(--brand-yellow)"/>
    </svg>

    <h1 class="sale-heading">FOR SALE</h1>

    <div class="agency-name">
      <span class="agency-title">FAIRBROOK &amp; CO</span>
      <span class="agency-sub">REAL ESTATE</span>
    </div>

    <div class="agent-photo" role="img" aria-label="Portrait photo of the listing agent in a blue pinstripe suit"></div>

    <p class="agent-name">DANIEL HART</p>
    <p class="agent-phone">0412 387 206</p>
  </div>
</body>
</html>
```